Cover Page Design

Create a new cover page in a sleek modern look that consists of our logo as provided. This cover page will be used in presentations and should only have colors featured in our branding efforts.

Target Market(s)

Architectural and Interior Design Clients

Industry/Entity Type

Interior Design

Font styles to use
Other font styles liked:
• see attached logo

Colors

Designer to choose colors to be used in the design.

Requirements
Must have
• Clean look, no pictures. just logo.
Nice to have
• colors that relate to our brand.
Should not have
• No colors not featured in our branding:
• www.velmacardwick.com

```html
<!DOCTYPE html>
<html lang="en">
<head>
<meta charset="utf-8">
<title>Velma Cardwick + Partners — Presentation Cover</title>
<link rel="stylesheet" href="https://fonts.googleapis.com/css2?family=Arimo:wght@400&display=swap">
<style>
  :root {
    --paper: #e3e3e3;
    --blue-pale: #9bbdef;
    --blue-mid: #5b9cf6;
    --blue-brand: #1677ff;
    --ink: #1c1c1c;
    --dot: #e3e3e3;
  }
  html, body {
    margin: 0;
    padding: 0;
    overflow: hidden;
    background: var(--paper);
  }
  .cover {
    position: relative;
    width: 798px;
    height: 1200px;
    background: var(--paper);
    overflow: hidden;
    font-family: "Arimo", Arial, sans-serif;
  }
  .cover__bands {
    position: absolute;
    inset: 0;
    width: 798px;
    height: 1200px;
  }
  .band--pale { fill: var(--blue-pale); }
  .band--mid { fill: var(--blue-mid); }
  .band--brand { fill: var(--blue-brand); }
  .pager-dot { fill: var(--dot); }

  .brand {
    position: absolute;
    top: 48px;
    right: 40px;
    display: flex;
    flex-direction: column;
    align-items: flex-end;
    color: var(--ink);
  }
  .brand__name {
    margin: 0;
    font-size: 28px;
    font-weight: 400;
    line-height: 1.1;
    white-space: nowrap;
    color: var(--ink);
  }
  .brand__tagline {
    margin: 16px 0 0;
    font-size: 12px;
    letter-spacing: 2.5px;
    text-transform: uppercase;
    white-space: nowrap;
    color: var(--ink);
  }
</style>
</head>
<body>
  <main class="cover">
    <svg class="cover__bands" viewBox="0 0 798 1200" aria-hidden="true">
      <polygon class="band--pale" points="0,206 590,563 552,588 0,253"/>
      <polygon class="band--mid" points="0,266 544,597 402,691 0,438"/>
      <polygon class="band--brand" points="0,438 798,944 798,1200 560,1200 0,844"/>
      <circle class="pager-dot" cx="535" cy="1077" r="18"/>
      <circle class="pager-dot" cx="615" cy="1077" r="18"/>
      <circle class="pager-dot" cx="695" cy="1077" r="18"/>
    </svg>

    <header class="brand">
      <h1 class="brand__name">Velma Cardwick + Partners</h1>
      <p class="brand__tagline">Architecture &amp; Interior Design</p>
    </header>
  </main>
</body>
</html>
```